New word press website site design

We provide email marketing to aircraft brokers and dealers to assist in finding buyers for their aircraft.

Our target market to purchase our broadcasts are the aircraft sellers – NOT the buyers.

Our target market when sending the email broadcast, are the buyers (end users).

The website should target brokers and our email database targets the buyers.

We do not buy or sell aircraft as a company. We provide email marketing solutions to connect buyers and sellers of aircraft.

Our other site is planevista.net and will be redesigned soon. Please use it as a reference as far as general scope but they layout can be completely different and should include helicopters only as far as imagery. The colors should be similar as the logos are similar, however we do NOT want both sites to be identical in use of primary color

Plenty of images and sample broadcasts attached to use as needed throughout the site.

Headlines listed below with some text copy.

In the event that we need to add more text, please use standard greek text as a place holder for the purposes of the mockup design.

Need to have a “SUBSCRIBE” button to join our mailing list.

Possible Headlines:

Exclusively Showcasing Rotor Wing Aircraft to the Global Marketplace

Showcasing Pre-Owned Helicopters Available For Sale, Lease, Trade, or Wanted for Acquisition.

Mobile-optimized Email Campaigns that Render Correctly Across all Devices

Targeted worldwide recipients that currently own, operate, or have an interest in rotor wing aircraft

STRONGEST Rotor Wing Database in the Industry

Text/Copy:

HOME
Rotorcraft Parade is one of most powerful marketing tools in the industry to utilize in reaching targeted buyers of pre-owned helicopters. Rotorcraft Parade provides the rotor wing aircraft market with a fast, effective, and affordable email broadcast solution to utilize in the marketing of Helicopters for sale.

Developed Exclusively to Showcase Rotor Wing Aircraft to the Global marketplace, Rotorcraft Parade is a powerful tool designed to maximize leads and accelerate the sales process by providing the ability to reach a global network of Helicopter buyers in a matter of seconds.

DATABASE:

While Rotorcraft Parade is delivered to all known broker/dealers, our primary focus is in reaching end users. Our opt-in/opt-out recipient database is updated daily and developed specifically to deliver the latest details on helicopters available for sale or lease to the inboxes of a global network of Helicopter buyers and sellers.

· Helicopter Owners

· Helicopter Operators

· Helicopter Charter Services

· Helicopter Management Companies

· Corporate/Municipal Flight Departments

· Helicopter Pilots

· Senior Aviation Executives

· Wealth Management Firms

· High Net Worth Individuals

· Helicopter Broker/Dealers

Helicopter Tour/Travel Firms

· Off Shore Oil & Gas Production Firms

· Municipalities/Media/Medevac Firms

Our recipient database is continuously updated and developed specifically to reach buyers and sellers of Helicopters. This ensures that your Helicopter will be showcased to the right people. Rotorcraft Parade does not broadcast non-rotor wing aircraft and focuses exclusively on the Global Helicopter Market.

Broadcast Design:

Rotorcraft Parade broadcast ads are custom designed for you by incorporating your corporate image and branding. Because you have worked hard in developing your corporate image, we strive to maintain it while designing an ad that will showcase your Helicopter to its best advantage. Rotorcraft Parade utilizes Mobile-optimized Email Campaigns with Responsive Coding to render correctly across all devices

Once you have approved the design, we schedule the broadcast to be sent on the available date and time you request. The broadcast will link to your website and the results can be immediate. All email leads and replies will go to the email address that you provided.

Pricing:
Create a place holder for 3 Different Broadcast Packages

-Broadcast Package A
-Broadcast Package B
-Broadcast Package C

Target Market(s)

The target market is any person or company that has aircraft for sale. We work with brokers, dealers, and owners to assist in finding buyers for their aircraft using email marketing campaigns (Parade broadcasts).

Industry/Entity Type

Aviation

Colors
0255a3
00a990

Requirements
Nice to have
• Samples of helicopter for sale broadcast ads in /image gallery/slider

```html
<!DOCTYPE html>
<html lang="en">
<head>
<meta charset="utf-8">
<title>Rotorcraft Parade</title>
<link rel="stylesheet" href="https://fonts.googleapis.com/css2?family=Cinzel:wght@400;600;700&family=Lora:wght@400;600&family=Open+Sans:wght@400;600&display=swap">
<style>
:root{
  --green:#5a9e3a;
  --green-dark:#3e8426;
  --navy:#0f2540;
  --ink:#222;
  --white:#fff;
  --footer:#1c1c1c;
  --footer-base:#121212;
}
*{box-sizing:border-box;margin:0;padding:0}
html,body{width:1200px;height:3475px;overflow:hidden}
body{position:relative;background:var(--white);font-family:"Lora",Georgia,serif;color:var(--ink)}

/* header */
.site-header{position:absolute;left:0;top:0;width:1200px;height:162px;background:linear-gradient(#3a3a3a,#1e1e1e)}
.brand{position:absolute;left:93px;top:52px;display:flex;align-items:center;gap:12px;font-family:"Cinzel",serif;font-weight:400;font-size:38px;color:var(--white);letter-spacing:1px}
.brand-dot{width:18px;height:18px;border-radius:50%;background:var(--green)}
.subscribe-pill{position:absolute;left:776px;top:30px;width:336px;height:51px;border-radius:26px;background:var(--green);display:flex;align-items:center;color:var(--white);font-family:"Cinzel",serif;font-size:17px;letter-spacing:.5px;white-space:nowrap}
.pill-icon{width:51px;height:51px;border-radius:50%;background:var(--green-dark);display:flex;align-items:center;justify-content:center;margin-right:18px;border:3px solid #f3f3f3;flex:none}
.main-nav{position:absolute;right:88px;top:106px;display:flex;font-family:"Cinzel",serif;font-size:16px;color:var(--white)}
.main-nav span{padding:0 22px;border-left:1px solid #aaa;line-height:18px}
.main-nav span:first-child{border-left:none}
.main-nav span:last-child{padding-right:0}

/* hero */
.hero{position:absolute;left:0;top:162px;width:1200px;height:533px;overflow:hidden}
.hero-photo{position:absolute;inset:0;background:linear-gradient(180deg,#5a5f66 0%,#8d7a5c 40%,#d99a4a 58%,#6d5a36 72%,#2f3a22 100%)}
.hero-stripe{position:absolute;left:0;top:0}
.slider-arrow{position:absolute;top:250px;width:34px;height:34px;border-radius:50%;background:rgba(255,255,255,.35);display:flex;align-items:center;justify-content:center}
.hero-title{position:absolute;left:86px;top:378px;font-family:"Cinzel",serif;color:var(--white);text-shadow:0 2px 4px rgba(0,0,0,.5)}
.hero-title .big{display:block;font-size:60px;font-weight:600;letter-spacing:2px;line-height:68px}
.hero-title .sub{display:block;font-size:35px;font-weight:600;letter-spacing:1px;line-height:44px}

/* about */
.about{position:absolute;left:0;top:695px;width:1200px;height:400px;overflow:hidden}
.about-photo{position:absolute;inset:0;background:linear-gradient(180deg,#2a2c2f,#3b3f42 60%,#23262a)}
.section-title{font-family:"Cinzel",serif;font-weight:400;text-align:center}
.about h2{position:absolute;left:0;right:0;top:46px;font-size:46px;color:var(--white)}
.about p{position:absolute;left:100px;width:1000px;top:120px;text-align:center;color:var(--white);font-size:14.5px;line-height:24px}
.btn-pill{position:absolute;height:46px;border-radius:23px;background:var(--green);display:flex;align-items:center;padding-right:22px;color:var(--white);font-family:"Cinzel",serif;font-size:13px;white-space:nowrap}
.btn-pill .pill-icon{width:46px;height:46px;margin-right:14px}
.about-cut{position:absolute;left:0;bottom:0}

/* database */
.database{position:absolute;left:0;top:1095px;width:1200px;height:615px}
.heli-shot{position:absolute;border-radius:4px}
.database h2{position:absolute;left:521px;top:120px;font-family:"Cinzel",serif;font-weight:400;font-size:26px;letter-spacing:1px}
.database p{position:absolute;left:521px;top:168px;width:600px;font-size:14.5px;line-height:23px}
.aud-list{position:absolute;top:312px;list-style:none;font-size:14.5px}
.aud-list li{height:30px;display:flex;align-items:center;gap:12px}
.bullet{width:16px;height:16px;border-radius:50%;background:var(--green);display:flex;align-items:center;justify-content:center;flex:none}

/* broadcast */
.broadcast{position:absolute;left:0;top:1710px;width:1200px;height:700px;overflow:hidden}
.broadcast-photo{position:absolute;inset:0;background:linear-gradient(180deg,#2c3136,#3a4047 55%,#1f2326)}
.broadcast h2{position:absolute;left:0;right:0;top:36px;font-size:29px;color:var(--white)}
.broadcast p{position:absolute;left:90px;width:1020px;text-align:center;color:var(--white);font-size:14.5px;line-height:24px}
.sample{position:absolute;top:278px;height:276px;border:2px solid #4d7a33;background:#000;padding:10px}
.sample div{width:100%;height:100%}

/* pricing */
.pricing{position:absolute;left:0;top:2410px;width:1200px;height:683px}
.pricing h2{position:absolute;left:0;right:0;top:36px;font-size:27px;letter-spacing:1px}
.pricing p{position:absolute;left:90px;width:1020px;top:84px;text-align:center;font-size:14.5px;line-height:24px}
.plan{position:absolute;top:197px;width:300px;height:440px}
.plan-card{position:absolute;left:0;top:0}
.plan-head{position:absolute;left:-4px;top:0;width:308px;height:48px;color:var(--white);font-family:"Cinzel",serif;font-size:23px;display:flex;align-items:center;justify-content:center}
.plan ul{position:absolute;left:56px;top:76px;list-style:none;font-family:"Open Sans",sans-serif;font-size:13.5px}
.plan li{height:30px;display:flex;align-items:center;gap:14px}
.tick{width:18px;height:18px;flex:none}
.price{position:absolute;left:0;width:300px;top:222px;text-align:center;font-family:"Open Sans",sans-serif;font-weight:600;font-size:16px;line-height:24px}
.plan-btn{position:absolute;left:74px;top:282px;width:152px;height:42px;color:var(--white);font-family:"Open Sans",sans-serif;font-size:15px;display:flex;align-items:center;justify-content:center}

/* footer */
.site-footer{position:absolute;left:0;top:3093px;width:1200px;height:325px;background:var(--footer);color:var(--white)}
.site-footer h3{position:absolute;top:56px;font-family:"Cinzel",serif;font-weight:600;font-size:21px;letter-spacing:1px}
.field{position:absolute;background:var(--white);color:#777;font-family:"Open Sans",sans-serif;font-size:12px;padding:6px 8px}
.send-btn{position:absolute;left:294px;top:255px;width:130px;height:27px;background:var(--green);font-family:"Open Sans",sans-serif;font-size:12px;display:flex;align-items:center;justify-content:center}
.link-list{position:absolute;left:584px;top:110px;list-style:none;font-family:"Open Sans",sans-serif;font-size:13px}
.link-list li{height:34px;display:flex;align-items:center;gap:10px}
.link-list li::before{content:"";width:4px;height:4px;border-radius:50%;background:var(--white)}
.contact-line{position:absolute;left:899px;display:flex;align-items:center;gap:14px;font-family:"Open Sans",sans-serif;font-size:13.5px}
.social{position:absolute;top:234px;width:32px;height:32px;border-radius:50%;background:var(--green)}
.base-bar{position:absolute;left:0;top:3418px;width:1200px;height:57px;background:var(--footer-base);color:var(--white);font-family:"Open Sans",sans-serif;font-size:12px}
.base-bar span{position:absolute;left:86px;top:20px}
.to-top{position:absolute;right:90px;top:14px;width:30px;height:30px;background:#2e2e2e;display:flex;align-items:center;justify-content:center}
</style>
</head>
<body>

<header class="site-header">
  <div class="brand"><span class="brand-dot"></span>Rotorcraft Parade</div>
  <div class="subscribe-pill">
    <span class="pill-icon"><svg width="22" height="16" viewBox="0 0 22 16"><rect x="1" y="1" width="20" height="14" fill="#fff"/><path d="M1 1l10 8 10-8" fill="none" stroke="#3e8426" stroke-width="2"/></svg></span>
    SUBSCRIBE OUR MAILING LIST
  </div>
  <nav class="main-nav"><span>HOME</span><span>DATABASE</span><span>BROADCAST DESIGN</span><span>PRICING</span><span>CONTACT</span></nav>
</header>

<section class="hero">
  <div class="hero-photo" role="img" aria-label="Helicopter silhouetted on a grass airfield at sunset"></div>
  <svg class="hero-stripe" width="1200" height="533" viewBox="0 0 1200 533"><polygon points="935,0 1075,0 700,533 556,533" fill="var(--green)" opacity=".9"/></svg>
  <div class="slider-arrow" style="left:14px"><svg width="12" height="14" viewBox="0 0 12 14"><path d="M9 1L3 7l6 6" stroke="#fff" stroke-width="2" fill="none"/></svg></div>
  <div class="slider-arrow" style="right:14px"><svg width="12" height="14" viewBox="0 0 12 14"><path d="M3 1l6 6-6 6" stroke="#fff" stroke-width="2" fill="none"/></svg></div>
  <h1 class="hero-title"><span class="big">STRONGEST</span><span class="sub">ROTOR WING SALES DATABASE&nbsp; IN THE INDUSTRY</span></h1>
</section>

<section class="about">
  <div class="about-photo" role="img" aria-label="Darkened helicopter in flight behind the about text"></div>
  <h2 class="section-title">ABOUT</h2>
  <p>Rotorcraft Parade is one of most powerful marketing tools in the industry to utilize in reaching targeted buyers of pre-owned helicopters. Rotorcraft Parade provides the rotor wing aircraft market with a fast, effective, and affordable email broadcast solution to utilize in the marketing of Helicopters for sale. Developed Exclusively to Showcase Rotor Wing Aircraft to the Global marketplace,<br>Rotorcraft Parade is a powerful tool designed to maximize leads and accelerate the sales process by providing the ability to reach a global network of Helicopter buyers in a matter of seconds.</p>
  <div class="btn-pill" style="left:463px;top:276px">
    <span class="pill-icon"><svg width="20" height="14" viewBox="0 0 22 16"><rect x="1" y="1" width="20" height="14" fill="#fff"/><path d="M1 1l10 8 10-8" fill="none" stroke="#3e8426" stroke-width="2"/></svg></span>
    SUBSCRIBE OUR MAILING LIST
  </div>
  <svg class="about-cut" width="1200" height="90" viewBox="0 0 1200 90"><polygon points="0,84 603,60 1200,86 1200,90 0,90" fill="#fff"/></svg>
</section>

<section class="database">
  <div class="heli-shot" style="left:81px;top:40px;width:348px;height:232px;background:linear-gradient(135deg,#f4f6f8,#1f4f9a 45%,#e8ecf0 70%)" role="img" aria-label="Blue and white helicopter in side view"></div>
  <div class="heli-shot" style="left:70px;top:330px;width:417px;height:197px;background:linear-gradient(135deg,#f4f6f8,#d8dde3 45%,#1e3f78 75%,#f4f6f8)" role="img" aria-label="White helicopter with blue tail in side view"></div>
  <h2>DATABASE</h2>
  <p>While Rotorcraft Parade is delivered to all known broker/dealers, our primary focus is in reaching end users. Our opt-in/opt-out recipient database is updated daily and developed specifically to deliver the latest details on helicopters available for sale or lease to the inboxes of a global network of Helicopter buyers and sellers.</p>
  <ul class="aud-list" style="left:521px">
    <li><span class="bullet"><svg width="8" height="8" viewBox="0 0 8 8"><path d="M2 1l3 3-3 3" stroke="#fff" stroke-width="1.6" fill="none"/></svg></span>Helicopter Owners</li>
    <li><span class="bullet"><svg width="8" height="8" viewBox="0 0 8 8"><path d="M2 1l3 3-3 3" stroke="#fff" stroke-width="1.6" fill="none"/></svg></span>Helicopter Operators</li>
    <li><span class="bullet"><svg width="8" height="8" viewBox="0 0 8 8"><path d="M2 1l3 3-3 3" stroke="#fff" stroke-width="1.6" fill="none"/></svg></span>Helicopter Charter Services</li>
    <li><span class="bullet"><svg width="8" height="8" viewBox="0 0 8 8"><path d="M2 1l3 3-3 3" stroke="#fff" stroke-width="1.6" fill="none"/></svg></span>Helicopter Management Companies</li>
    <li><span class="bullet"><svg width="8" height="8" viewBox="0 0 8 8"><path d="M2 1l3 3-3 3" stroke="#fff" stroke-width="1.6" fill="none"/></svg></span>Corporate/Municipal Flight</li>
    <li><span class="bullet"><svg width="8" height="8" viewBox="0 0 8 8"><path d="M2 1l3 3-3 3" stroke="#fff" stroke-width="1.6" fill="none"/></svg></span>Departments</li>
    <li><span class="bullet"><svg width="8" height="8" viewBox="0 0 8 8"><path d="M2 1l3 3-3 3" stroke="#fff" stroke-width="1.6" fill="none"/></svg></span>Helicopter Pilots</li>
    <li><span class="bullet"><svg width="8" height="8" viewBox="0 0 8 8"><path d="M2 1l3 3-3 3" stroke="#fff" stroke-width="1.6" fill="none"/></svg></span>Senior Aviation Executives</li>
  </ul>
  <ul class="aud-list" style="left:834px">
    <li><span class="bullet"><svg width="8" height="8" viewBox="0 0 8 8"><path d="M2 1l3 3-3 3" stroke="#fff" stroke-width="1.6" fill="none"/></svg></span>Wealth Management Firms</li>
    <li><span class="bullet"><svg width="8" height="8" viewBox="0 0 8 8"><path d="M2 1l3 3-3 3" stroke="#fff" stroke-width="1.6" fill="none"/></svg></span>High Net Worth Individuals</li>
    <li><span class="bullet"><svg width="8" height="8" viewBox="0 0 8 8"><path d="M2 1l3 3-3 3" stroke="#fff" stroke-width="1.6" fill="none"/></svg></span>Helicopter Broker/Dealers</li>
    <li><span class="bullet"><svg width="8" height="8" viewBox="0 0 8 8"><path d="M2 1l3 3-3 3" stroke="#fff" stroke-width="1.6" fill="none"/></svg></span>Helicopter Tour/Travel Firms</li>
    <li><span class="bullet"><svg width="8" height="8" viewBox="0 0 8 8"><path d="M2 1l3 3-3 3" stroke="#fff" stroke-width="1.6" fill="none"/></svg></span>Off Shore Oil &amp; Gas Production Firms</li>
    <li><span class="bullet"><svg width="8" height="8" viewBox="0 0 8 8"><path d="M2 1l3 3-3 3" stroke="#fff" stroke-width="1.6" fill="none"/></svg></span>Municipalities/Media/Medevac Firms</li>
  </ul>
</section>

<section class="broadcast">
  <div class="broadcast-photo" role="img" aria-label="Darkened fleet of helicopters on an apron"></div>
  <h2 class="section-title">Broadcast Design</h2>
  <p style="top:90px">Rotorcraft Parade broadcast ads are custom designed for you by incorporating your corporate image and branding. Because you have worked hard in developing your corporate image, we strive to maintain it while designing an ad that will showcase your Helicopter to its best advantage. Rotorcraft Parade utilizes Mobile-optimized Email Campaigns with Responsive Coding to render correctly across all devices</p>
  <p style="top:200px">Once you have approved the design, we schedule the broadcast to be sent on the available date and time you request. The broadcast will link to your website and the results can be immediate. All email leads and replies will go to the email address that you provided.</p>
  <div class="sample" style="left:116px;width:289px"><div role="img" aria-label="Sample broadcast ad for a helicopter for sale" style="background:linear-gradient(180deg,#f2f2f2 0 18%,#c23a2f 18% 26%,#6f8596 26% 62%,#f2f2f2 62%)"></div></div>
  <div class="sample" style="left:470px;width:260px"><div role="img" aria-label="Sample wanted-to-buy helicopter broadcast ad" style="background:linear-gradient(180deg,#000 0 40%,#d8d8d8 40% 75%,#000 75%)"></div></div>
  <div class="sample" style="left:829px;width:260px"><div role="img" aria-label="Sample broadcast ad showcasing a utility helicopter" style="background:linear-gradient(180deg,#e25a1c 0 10%,#6b6e70 10% 38%,#e8e8e8 38%)"></div></div>
  <div class="btn-pill" style="left:483px;top:596px">
    <span class="pill-icon"><svg width="20" height="14" viewBox="0 0 22 16"><rect x="1" y="1" width="20" height="14" fill="#fff"/><path d="M1 1l10 8 10-8" fill="none" stroke="#3e8426" stroke-width="2"/></svg></span>
    REQUEST DESIGN PROOF
  </div>
</section>

<section class="pricing">
  <h2 class="section-title">Pricing</h2>
  <p>Lorem Ipsum is simply dummy text of the printing and typesetting industry. Lorem Ipsum has been the industry's standard dummy text ever since the 1500s, when an unknown printer took a galley of type and scrambled it to make a type specimen book.</p>

  <div class="plan" style="left:134px">
    <svg class="plan-card" width="316" height="450" viewBox="0 0 316 450"><polygon points="14,14 314,14 314,356 164,446 14,356" fill="#d9d9d9"/><polygon points="0,0 300,0 300,342 150,432 0,342" fill="#fff" stroke="#eee"/></svg>
    <div class="plan-head" style="background:var(--green)">Broadcast Package A</div>
    <ul>
      <li><svg class="tick" viewBox="0 0 18 18"><circle cx="9" cy="9" r="9" fill="var(--green)"/><path d="M5 9l3 3 5-6" stroke="#fff" stroke-width="2" fill="none"/></svg>Lorem Ipsum is dummy.</li>
      <li><svg class="tick" viewBox="0 0 18 18"><circle cx="9" cy="9" r="9" fill="var(--green)"/><path d="M5 9l3 3 5-6" stroke="#fff" stroke-width="2" fill="none"/></svg>Lorem Ipsum is dummy.</li>
      <li><svg class="tick" viewBox="0 0 18 18"><circle cx="9" cy="9" r="9" fill="var(--green)"/><path d="M5 9l3 3 5-6" stroke="#fff" stroke-width="2" fill="none"/></svg>Lorem Ipsum is dummy.</li>
    </ul>
    <div class="price">PRICE START AT:<br>$59 USD</div>
    <div class="plan-btn" style="background:var(--green)">SUBSCRIBE</div>
  </div>

  <div class="plan" style="left:452px;top:185px">
    <svg class="plan-card" width="316" height="450" viewBox="0 0 316 450"><polygon points="14,14 314,14 314,356 164,446 14,356" fill="#d9d9d9"/><polygon points="0,0 300,0 300,342 150,432 0,342" fill="#fff" stroke="#eee"/></svg>
    <div class="plan-head" style="background:var(--navy)">Broadcast Package B</div>
    <ul>
      <li><svg class="tick" viewBox="0 0 18 18"><circle cx="9" cy="9" r="9" fill="var(--green)"/><path d="M5 9l3 3 5-6" stroke="#fff" stroke-width="2" fill="none"/></svg>Lorem Ipsum is dummy.</li>
      <li><svg class="tick" viewBox="0 0 18 18"><circle cx="9" cy="9" r="9" fill="var(--green)"/><path d="M5 9l3 3 5-6" stroke="#fff" stroke-width="2" fill="none"/></svg>Lorem Ipsum is dummy.</li>
    </ul>
    <div class="price" style="top:234px">PRICE START AT:<br>$149 USD</div>
    <div class="plan-btn" style="background:var(--navy);top:294px">SUBSCRIBE</div>
  </div>

  <div class="plan" style="left:765px">
    <svg class="plan-card" width="316" height="450" viewBox="0 0 316 450"><polygon points="14,14 314,14 314,356 164,446 14,356" fill="#d9d9d9"/><polygon points="0,0 300,0 300,342 150,432 0,342" fill="#fff" stroke="#eee"/></svg>
    <div class="plan-head" style="background:var(--green)">Broadcast Package C</div>
    <ul>
      <li><svg class="tick" viewBox="0 0 18 18"><circle cx="9" cy="9" r="9" fill="var(--green)"/><path d="M5 9l3 3 5-6" stroke="#fff" stroke-width="2" fill="none"/></svg>Lorem Ipsum is dummy.</li>
      <li><svg class="tick" viewBox="0 0 18 18"><circle cx="9" cy="9" r="9" fill="var(--green)"/><path d="M5 9l3 3 5-6" stroke="#fff" stroke-width="2" fill="none"/></svg>Lorem Ipsum is dummy.</li>
      <li><svg class="tick" viewBox="0 0 18 18"><circle cx="9" cy="9" r="9" fill="var(--green)"/><path d="M5 9l3 3 5-6" stroke="#fff" stroke-width="2" fill="none"/></svg>Lorem Ipsum is dummy.</li>
    </ul>
    <div class="price">PRICE START AT:<br>$549 USD</div>
    <div class="plan-btn" style="background:var(--green)">SUBSCRIBE</div>
  </div>
</section>

<footer class="site-footer">
  <h3 style="left:86px">SEND MESSAGE</h3>
  <div class="field" style="left:86px;top:115px;width:160px;height:29px">NAME</div>
  <div class="field" style="left:264px;top:115px;width:160px;height:29px">EMAIL</div>
  <div class="field" style="left:86px;top:151px;width:338px;height:93px">MESSAGE</div>
  <div class="send-btn">SEND MESSAGE</div>

  <h3 style="left:584px">SITE LINKS</h3>
  <ul class="link-list"><li>HOME</li><li>DATABASE</li><li>BROADCAST DESIGN</li><li>PRICING</li><li>CONTACT</li></ul>

  <h3 style="left:899px">CONTACT US</h3>
  <div class="contact-line" style="top:110px"><svg width="14" height="18" viewBox="0 0 14 18"><path d="M7 0C3 0 0 3 0 7c0 5 7 11 7 11s7-6 7-11c0-4-3-7-7-7z" fill="var(--green)"/><circle cx="7" cy="7" r="2.5" fill="var(--footer)"/></svg>Alder Springs, Texas 77000</div>
  <div class="contact-line" style="top:160px"><svg width="18" height="13" viewBox="0 0 18 13"><rect width="18" height="13" fill="var(--green)"/><path d="M0 0l9 7 9-7" stroke="var(--footer)" stroke-width="1.5" fill="none"/></svg>info@rotorcraftparade.net</div>
  <div class="social" style="left:893px"></div>
  <div class="social" style="left:933px"></div>
</footer>
<div class="base-bar"><span>2018 © rotorcraftparade.net. All Rights Reserved.</span><div class="to-top"><svg width="12" height="8" viewBox="0 0 12 8"><path d="M1 7l5-5 5 5" stroke="#fff" stroke-width="2" fill="none"/></svg></div></div>

</body>
</html>
```